Lou Brennigan Party invite for 8/20/2018

Lou Brennigan is returning to downtown Jacksonport for another night of fun at Twelve Bells Tavern. Bring a date and tell your friends! Monday, August 20, 2018.
The party starts at 7 pm with limo rides home starting at 11:30.

Target Market(s)

our friends- we will be mailing out this invite

Colors

Designer to choose colors to be used in the design.

Requirements
Must have
• 2 sided postcard for mailing invite
Nice to have
• fun party layout- use the images provides and whatever else you think

```html
<!DOCTYPE html>
<html lang="en">
<head>
<meta charset="utf-8">
<title>Lou Brennigan Live – Party Invite Postcard</title>
<link rel="stylesheet" href="https://fonts.googleapis.com/css2?family=Oswald:wght@400;500&family=Courgette&display=swap">
<style>
  :root {
    --page: #ece6dd;
    --crimson: #b0173f;
    --crimson-deep: #7e0d2c;
    --gold: #f2b534;
    --gold-light: #ffd95a;
    --orange: #ec5a1c;
    --yellow: #f6d21c;
    --ink: #1d1d1f;
    --red-text: #e2231a;
    --white: #ffffff;
    --card-white: #fbfbfb;
    --line-grey: #c9c9c9;
    --brand-dot: #5a3a2c;
  }
  * { box-sizing: border-box; margin: 0; padding: 0; }
  html, body { width: 1200px; height: 729px; overflow: hidden; }
  body { background: var(--page); position: relative; font-family: "Oswald", sans-serif; }

  .postcard {
    position: absolute; top: 180px; width: 560px; height: 368px;
    overflow: hidden; box-shadow: 0 6px 18px rgba(0,0,0,.18);
  }
  .postcard--back { left: 30px; background: var(--card-white); }
  .postcard--front { left: 610px;
    background: radial-gradient(circle at 55% 35%, #e0365e 0%, var(--crimson) 45%, var(--crimson-deep) 100%); }

  /* shared event text */
  .event-date { font-weight: 400; font-size: 24px; line-height: 1; color: var(--ink); }
  .event-venue { font-weight: 400; font-size: 21px; line-height: 1.02; color: var(--red-text); text-transform: uppercase; margin-top: 4px; }
  .event-place { font-family: "Courgette", cursive; font-size: 11px; color: var(--ink); margin-top: 3px; }

  .ring { position: absolute; }

  .brand { position: absolute; display: flex; align-items: center; gap: 7px; }
  .brand__dot { width: 34px; height: 34px; border-radius: 50%; background: var(--brand-dot); flex: none; }
  .brand__name { font-weight: 500; font-size: 19px; color: var(--white); white-space: nowrap; }

  /* back side */
  .back-art {
    position: absolute; left: 0; top: 0; width: 375px; height: 310px;
    background: radial-gradient(circle at 55% 50%, #d62a52 0%, var(--crimson) 50%, var(--crimson-deep) 100%);
  }
  .back-art .ring { left: 85px; top: 45px; width: 230px; height: 230px; }
  .back-text { position: absolute; left: 115px; top: 105px; width: 170px; text-align: center; }
  .back-art .brand { left: 14px; top: 14px; }

  .stamp-box { position: absolute; right: 12px; top: 12px; width: 78px; height: 88px; border: 1px solid var(--line-grey); }
  .address-lines { position: absolute; left: 400px; top: 180px; width: 145px; }
  .address-lines span { display: block; height: 30px; border-bottom: 1px solid var(--line-grey); }

  /* front side */
  .front-art { position: absolute; inset: 0; }
  .front-art .ring { left: 160px; top: 20px; width: 240px; height: 240px; }
  .performer-photo {
    position: absolute; left: 205px; top: 62px; width: 150px; height: 306px;
    border-radius: 75px 75px 0 0;
    background: linear-gradient(180deg, #c79b82 0%, #b58a70 22%, #2a2a2c 34%, #1f1f21 70%, #a8632c 100%);
  }
  .front-text { position: absolute; left: 195px; top: 150px; width: 170px; text-align: center; }
  .front-text .event-date { color: var(--white); font-size: 22px; }
  .front-text .event-venue { color: var(--gold-light); font-size: 19px; }
  .front-text .event-place { color: var(--white); }
  .postcard--front .brand { right: 10px; top: 110px; gap: 6px; }
  .postcard--front .brand__dot { width: 28px; height: 28px; }
  .postcard--front .brand__name { font-size: 17px; }

  .tagline-band {
    position: absolute; left: 0; top: 318px; width: 200px; height: 34px;
    background: var(--orange); display: flex; align-items: center; padding-left: 10px;
    font-family: "Courgette", cursive; font-size: 11.5px; color: var(--white); white-space: nowrap;
  }
  .time-band {
    position: absolute; right: 0; top: 300px; width: 180px; height: 68px;
    background: var(--yellow); padding: 16px 10px 0 14px;
  }
  .time-band__main { font-weight: 500; font-size: 12px; color: var(--red-text); line-height: 1.1; white-space: nowrap; }
  .time-band__sub { font-weight: 400; font-size: 7.5px; color: var(--ink); margin-top: 3px; white-space: nowrap; }
</style>
</head>
<body>

<section class="postcard postcard--back" aria-label="Postcard, address side">
  <div class="back-art">
    <svg class="ring" viewBox="0 0 230 230" aria-hidden="true">
      <circle cx="115" cy="115" r="108" fill="none" stroke="#e9582a" stroke-width="14"/>
      <circle cx="115" cy="115" r="108" fill="none" stroke="#fff6d8" stroke-width="7" stroke-linecap="round" stroke-dasharray="0 22.6"/>
      <circle cx="115" cy="115" r="98" fill="var(--white)"/>
    </svg>
    <div class="brand">
      <span class="brand__dot"></span>
      <span class="brand__name">Lou Brennigan</span>
    </div>
    <div class="back-text">
      <p class="event-date">20/08/2018</p>
      <p class="event-venue">Twelve Bells<br>Tavern</p>
      <p class="event-place">downtown Jacksonport</p>
    </div>
  </div>
  <div class="stamp-box"></div>
  <div class="address-lines"><span></span><span></span><span></span><span></span></div>
</section>

<section class="postcard postcard--front" aria-label="Postcard, picture side">
  <div class="front-art">
    <svg width="560" height="368" viewBox="0 0 560 368" style="position:absolute;left:0;top:0" aria-hidden="true">
      <path d="M0 250 C120 200 250 230 560 170 L560 368 L0 368 Z" fill="var(--gold)"/>
      <path d="M0 285 C140 245 280 270 560 230 L560 368 L0 368 Z" fill="var(--yellow)" opacity=".8"/>
    </svg>
    <svg class="ring" viewBox="0 0 240 240" aria-hidden="true">
      <circle cx="120" cy="120" r="112" fill="none" stroke="#e9582a" stroke-width="14"/>
      <circle cx="120" cy="120" r="112" fill="none" stroke="#fff6d8" stroke-width="7" stroke-linecap="round" stroke-dasharray="0 22"/>
      <circle cx="120" cy="120" r="102" fill="#f4eee8"/>
    </svg>
    <div class="performer-photo" role="img" aria-label="Photo of the singer playing an acoustic guitar"></div>
  </div>
  <div class="front-text">
    <p class="event-date">20/08/2018</p>
    <p class="event-venue">Twelve Bells<br>Tavern</p>
    <p class="event-place">downtown Jacksonport</p>
  </div>
  <div class="brand">
    <span class="brand__dot"></span>
    <span class="brand__name">Lou Brennigan</span>
  </div>
  <p class="tagline-band">Bring a date and tell your friends!</p>
  <div class="time-band">
    <p class="time-band__main">THE PARTY STARTS AT 7 PM</p>
    <p class="time-band__sub">WITH LIMO RIDES HOME STARTING AT 11:30.</p>
  </div>
</section>

</body>
</html>
```